New Website for ReBranded Company - CrewBeacon

We have a successful company and website currently but it is a little dated. We have re-branded the company from Harbor Signal Networks to CrewBeacon and have a new logo for the new name. We are looking to build a newer fresher website with the new name. I will need a concept of the home page and one inside page. You can see our current site at https://www.harborsignalnetworks.example and the new site will be https://www.crewbeacon.example .

I also really like the https://www.pathlantern.example/ website. I like ledgerkite.example website. I like the https://skillorbit.example/ website.

See the attached document for layout and some text to use. Use the pictures I attached as opposed to pictures from the old site as much as you can.

Target Market(s)

Business

Industry/Entity Type

Software Service

Number of Pages Required

2 page

Font styles to use
Sans Serif

Requirements
Must have
• Use the colors from my logo. Professional but modern. We want people to feel like our product makes their staff feel safer at work.
Should not have
• Don't use any red or orange (no stop colors).

```html
<!DOCTYPE html>
<html lang="en">
<head>
<meta charset="utf-8">
<title>CrewBeacon – Home and Demo pages</title>
<link href="https://fonts.googleapis.com/css2?family=Roboto:wght@400;500;700&display=swap" rel="stylesheet">
<style>
:root{
  --blue:#3a95d3;
  --blue-deep:#2f86c6;
  --blue-pale:#a9d0ee;
  --green:#63a925;
  --ink:#111;
  --white:#fff;
  --frame:#333;
}
*{margin:0;padding:0;box-sizing:border-box}
html,body{width:803px;height:1200px;overflow:hidden;background:var(--white)}
body{position:relative;font-family:'Roboto',Arial,sans-serif;color:var(--ink)}
.page{position:absolute;border:1px solid var(--frame);background:var(--white);overflow:hidden}
.page-home{left:51px;top:41px;width:323px;height:1127px}
.page-demo{left:432px;top:44px;width:322px;height:517px}
.abs{position:absolute}
.brand{position:absolute;display:flex;align-items:center;gap:4px;font-weight:500;color:var(--blue)}
.brand-dot{border-radius:50%;background:var(--blue)}
.nav{position:absolute;display:flex;gap:6px;font-size:4.2px;color:#222}
.nav .active{color:var(--blue);text-decoration:underline}
.photo{position:absolute}
.btn{position:absolute;display:flex;align-items:center;justify-content:center;background:var(--green);color:var(--white);font-size:6px}
.center{text-align:center}
.hero-title{font-size:13px;line-height:15.5px;color:#111}
.hero-title b{font-weight:700}
.feature-box{position:absolute;top:180px;width:77px;height:53px;background:var(--green);color:var(--white);border-radius:3px;font-size:6.2px;line-height:8px;display:flex;align-items:center;justify-content:center;text-align:center;padding:0 6px}
.band{position:absolute;left:0;width:100%;background:var(--green)}
.tile-blue{position:absolute;background:var(--blue);color:var(--white)}
.tile-title{font-size:8px;font-weight:500;letter-spacing:.2px}
.tile-text{font-size:4.3px;line-height:8px}
.icon{width:17px;height:17px}
.options{display:grid;grid-template-columns:52px 48px 40px;font-size:4.4px;row-gap:3px}
.plan-col h3{font-size:8px;line-height:8px;font-weight:700}
.plan-col p{font-size:6.2px;line-height:8px}
.plan-num{font-size:8px;color:var(--white);font-weight:700}
.footer{position:absolute;left:0;width:100%;background:var(--blue);color:var(--white)}
.footer h4{font-size:6.2px;font-weight:700;margin-bottom:6px}
.footer p,.footer li{font-size:3.9px;line-height:6.4px;list-style:none}
.copyright{position:absolute;font-size:2.8px;font-weight:700}
.demo-h{font-size:7.8px;line-height:9.5px;color:var(--blue);font-weight:500;margin-bottom:8px}
.demo-p{font-size:4.4px;line-height:5.8px;margin-bottom:6px}
.link-green{color:var(--green)}
</style>
</head>
<body>

<!-- Home page -->
<section class="page page-home">
  <header>
    <div class="brand" style="left:33px;top:9px;font-size:11px"><span class="brand-dot" style="width:18px;height:18px"></span>CrewBeacon</div>
    <nav class="nav" style="left:168px;top:21px">
      <span class="active">Home</span><span>Buy Addons</span><span>Customer Login</span><span>Explore Your Choices</span>
    </nav>
  </header>

  <div class="photo" role="img" aria-label="Hand pressing a panic button mounted under a desk, tinted blue" style="left:0;top:40px;width:323px;height:148px;background:linear-gradient(120deg,#6fb0e0,#b8dbf3 55%,#8cc3ea)"></div>
  <div class="abs center hero-title" style="left:0;width:323px;top:77px">FEEL <b>CONFIDENT</b> THAT<br>YOUR STAFF IS <b>PROTECTED</b></div>
  <div class="abs center" style="left:0;width:323px;top:118px;font-size:9px">Get a revolutionary new electronic panic button</div>
  <div class="btn" style="left:125px;top:150px;width:73px;height:14px">Ready To Get Started</div>

  <div class="feature-box" style="left:34px">Problems Stopped Before They Start For Any Type Of Organization</div>
  <div class="feature-box" style="left:124px">Affordable Prices Starting at $18 per month. No Contracts. No Hidden Costs.</div>
  <div class="feature-box" style="left:213px">Alerts by computer, mobile device, text, phone, email, monitoring and E911</div>

  <h2 class="abs center" style="left:0;width:323px;top:258px;font-size:9.5px;line-height:10px;font-weight:700">YOUR EMPOYEES SHOULDN’T FEEL ALONE<br>WHEN THEY NEED HELP</h2>
  <p class="abs center" style="left:0;width:323px;top:287px;font-size:6.3px;line-height:8px">Does this problem make you feel frustrated and anxious?<br>Put a simple solution in their hands.</p>
  <div class="btn" style="left:126px;top:307px;width:73px;height:14px">Ready To Get Started</div>

  <div class="band center" style="top:347px;height:29px;color:var(--white);font-size:13px;font-weight:700;line-height:29px">WHY BUSINESSES CHOOSE US</div>

  <div class="tile-blue" style="left:0;top:376px;width:162px;height:88px;padding:10px 0 0 28px">
    <svg class="icon" viewBox="0 0 20 20"><circle cx="10" cy="10" r="8.5" fill="none" stroke="#111" stroke-width="1.4"/><path d="M7 12l2-5 4 2-2 5z" fill="none" stroke="#111" stroke-width="1.2"/></svg>
    <div class="tile-title" style="margin-top:4px">EASY TO USE</div>
    <p class="tile-text" style="margin-top:6px;width:124px">Press a button and let the right people know you need help and open a chat window letting everyone talk on resolving their problem.</p>
  </div>
  <div class="photo" role="img" aria-label="Black two-button panic device" style="left:162px;top:376px;width:161px;height:88px;background:radial-gradient(circle at 55% 45%,#4a4a4a 0 22%,#fff 23%)"></div>

  <div class="photo" role="img" aria-label="Desktop monitor, laptop and phone showing the alert software" style="left:0;top:464px;width:162px;height:92px;background:radial-gradient(ellipse at 50% 50%,#5a6f8a 0 28%,#fff 30%)"></div>
  <div class="tile-blue" style="left:162px;top:464px;width:161px;height:92px;padding:9px 0 0 11px">
    <svg class="icon" viewBox="0 0 20 20"><path d="M4 4h12v8H9l-4 3v-3H4z" fill="none" stroke="#111" stroke-width="1.4"/><circle cx="8" cy="8" r="1" fill="#111"/><circle cx="11" cy="8" r="1" fill="#111"/><circle cx="14" cy="8" r="1" fill="#111"/></svg>
    <div class="tile-title" style="line-height:8px;margin-top:4px">COMMUNICATE THE WAY YOU<br>WANT</div>
    <p class="tile-text" style="line-height:6px;margin-top:1px">We give you lots of options:</p>
    <div class="options" style="margin-top:2px">
      <span>✓ Computer</span><span>✓ Phone call</span><span>✓ Call Center</span>
      <span>✓ Mobile</span><span>✓ Text</span><span></span>
      <span>✓ Email</span><span>✓ E911</span><span></span>
    </div>
  </div>

  <div class="tile-blue" style="left:0;top:556px;width:162px;height:88px;padding:12px 0 0 28px">
    <svg class="icon" viewBox="0 0 20 20"><circle cx="10" cy="10" r="8" fill="none" stroke="#111" stroke-width="1.4" stroke-dasharray="3 1.5"/><text x="10" y="14" font-size="11" text-anchor="middle" fill="#111" font-family="Roboto,Arial,sans-serif">$</text></svg>
    <div class="tile-title" style="margin-top:3px">COST EFFECTIVE PROTECTION</div>
    <p class="tile-text" style="margin-top:6px;width:130px">By leveraging your existing network and equipment we can lower your costs to give better options to your staff.</p>
  </div>
  <div class="photo" role="img" aria-label="Person slipping a panic button into a jeans pocket" style="left:162px;top:556px;width:161px;height:88px;background:linear-gradient(110deg,#2c3e5c,#3f5475 60%,#fff 61%)"></div>

  <div class="band" style="top:644px;height:30px"></div>
  <div class="abs center" style="left:112px;top:653px;width:98px;height:12px;background:var(--white);font-size:6px;line-height:12px">Ready to Get Started</div>

  <p class="abs center" style="left:0;width:323px;top:707px;font-size:6.2px;line-height:10px">We know how scary it can feel to worry about employee safety.<br>That’s why we have provided a way for customers to get help to staff effectively in</p>
  <p class="abs center" style="left:0;width:323px;top:733px;font-size:9.5px;font-weight:700"><span style="color:var(--blue)">45 States</span> <span style="font-size:6px;font-weight:400">covering</span> <span style="color:var(--green)">5 Countries</span></p>
  <div class="btn" style="left:110px;top:755px;width:102px;height:15px;font-size:7.6px">START MY DEMO</div>

  <div class="photo" role="img" aria-label="Desk phone and panic button on an office desk, tinted green" style="left:0;top:797px;width:323px;height:178px;background:linear-gradient(160deg,#c6e4a6,#a6d47a 50%,#d6ecc0)"></div>
  <h2 class="abs center" style="left:0;width:323px;top:815px;font-size:9.5px;font-weight:700">SIMPLE START PLAN</h2>
  <div class="abs plan-col" style="left:37px;top:836px;width:70px"><div class="plan-num">1</div><h3>Explore Your<br>Choices</h3><p style="margin-top:4px">Pricing<br>• Trial<br>• Quote<br>• Hardware</p></div>
  <div class="abs plan-col" style="left:121px;top:836px;width:80px"><div class="plan-num">2</div><h3>Get Setup</h3><p style="margin-top:4px">• Input Your Alerts<br>• Input Your Staff<br>• Install Our Software</p></div>
  <div class="abs plan-col" style="left:213px;top:836px;width:75px"><div class="plan-num">3</div><h3>Feel Confident<br>Your Staff Is<br>Protected</h3><p style="margin-top:4px">High Five. You just too a major step to getting rid of the anxiety and frustration this gave you.</p></div>
  <h2 class="abs center" style="left:0;width:323px;top:923px;font-size:9.5px;font-weight:700">Stay Connected with Staff during a Crisis Situations</h2>
  <div class="btn" style="left:108px;top:946px;width:102px;height:15px;font-size:7.6px;background:var(--blue)">START MY DEMO</div>

  <footer class="footer" style="top:975px;height:93px">
    <div class="abs" style="left:30px;top:14px;width:62px"><h4 style="margin-bottom:6px;line-height:7px">Call Us<br>1 - 800 - 555 - 0142</h4><p>When employees feel alone during a threatening situation, we give them a way to let the right resources know that they need help so you can feel confident that your staff is protected.</p></div>
    <div class="abs" style="left:103px;top:14px"><h4>SHOP</h4><ul><li>Add Ons</li><li>Start My Demo</li><li>Custom Quote</li><li>Start Trial</li></ul></div>
    <div class="abs" style="left:169px;top:14px"><h4>ABOUT</h4><ul><li>Affiliates</li><li>Contact</li><li>Support</li><li>Existing Customers</li><li>Industries</li><li>Blog</li><li>FAQ</li></ul></div>
    <div class="abs" style="left:238px;top:14px"><h4>LEGAL</h4><ul><li>Privacy Policy</li><li>Terms of Use</li><li>End User License</li><li>Agreement</li></ul></div>
  </footer>
  <div class="brand" style="left:30px;top:1074px;font-size:9px"><span class="brand-dot" style="width:15px;height:15px"></span>CrewBeacon</div>
  <div class="copyright" style="left:30px;top:1099px">©CrewBeacon 2020</div>
</section>

<!-- Demo page -->
<section class="page page-demo">
  <header>
    <div class="brand" style="left:33px;top:8px;font-size:11px"><span class="brand-dot" style="width:18px;height:18px"></span>CrewBeacon</div>
    <nav class="nav" style="left:167px;top:19px"><span>Home</span><span>Buy Addons</span><span>Customer Login</span><span>Explore Your Choices</span></nav>
  </header>
  <div class="photo" role="img" aria-label="Wall-mounted alarm box with push button, tinted blue" style="left:0;top:40px;width:322px;height:148px;background:linear-gradient(90deg,#5ca6dc,#86bfe8 45%,#d4e9f7 70%,#b3d6f0)"></div>
  <div class="abs" style="left:190px;top:72px;font-size:12.5px;line-height:16px">Curious How<br><b>Beacon Relay</b><br>Works?</div>
  <div class="btn" style="left:190px;top:139px;width:102px;height:12px;font-size:4.4px;font-weight:700">BOOK A LIVE DEMO TODAY</div>

  <div class="abs" style="left:34px;top:215px;width:118px">
    <h3 class="demo-h">What makes Beacon Relay so powerful?</h3>
    <p class="demo-p">Beacon Relay uses the power of the internet and your computer to let you communicate instantly with those around you in times of crisis. Sign up for the demo today and learn what makes our software so special!</p>
  </div>
  <div class="abs" style="left:177px;top:214px;width:122px">
    <h3 class="demo-h">Ready for Your Demo?</h3>
    <p class="demo-p">Do you have a committee or directors meeting concerning safety and security?</p>
    <p class="demo-p">We offer a live demo that is an in depth look at Beacon Relay. We can show you the ins and outs of our program and answer any questions you may have right on the spot.</p>
    <p class="demo-p">You can also <span class="link-green">sign up</span> for a free trial.</p>
    <p class="demo-p">This is a great opportunity for you to see how Beacon Relay works in your environment.</p>
  </div>
  <div class="btn" style="left:177px;top:306px;width:104px;height:11px;font-size:4.4px">Click HERE to book your live demo</div>
  <p class="abs demo-p" style="left:177px;top:327px;width:140px">Want to speak to a human? 1 800 555 0142<br>or email us at info@harborsignalnetworks.example</p>

  <footer class="footer" style="top:367px;height:93px">
    <div class="abs" style="left:31px;top:14px;width:62px"><h4 style="margin-bottom:6px;line-height:7px">Call Us<br>1 - 800 - 555 - 0142</h4><p>When employees feel alone during a threatening situation, we give them a way to let the right resources know that they need help so you can feel confident that your staff is protected.</p></div>
    <div class="abs" style="left:103px;top:14px"><h4>SHOP</h4><ul><li>Add Ons</li><li>Start My Demo</li><li>Custom Quote</li><li>Start Trial</li></ul></div>
    <div class="abs" style="left:170px;top:14px"><h4>ABOUT</h4><ul><li>Affiliates</li><li>Contact</li><li>Support</li><li>Existing Customers</li><li>Industries</li><li>Blog</li><li>FAQ</li></ul></div>
    <div class="abs" style="left:238px;top:14px"><h4>LEGAL</h4><ul><li>Privacy Policy</li><li>Terms of Use</li><li>End User License</li><li>Agreement</li></ul></div>
  </footer>
  <div class="brand" style="left:31px;top:466px;font-size:9px"><span class="brand-dot" style="width:15px;height:15px"></span>CrewBeacon</div>
  <div class="copyright" style="left:31px;top:491px">©CrewBeacon 2020</div>
</section>

</body>
</html>
```